Updated flyer

We've decided to do this as a house party, the info is below. For this you can use a model or not use one, either way is fine. I attached two logos and some designs we've used from pixel harbor before. I also attached a pic with a duck that you can use as the background
TIDE SWAY
(Pool Party Edition)
July 13 2013
Featuring DJs
Vantor (logo) Kemble (logo)
Lionel Hartwick Marty Oakes
brindlepage.com/vantor87 for address (Larkwood, invite only)
Full Bar/Food/Water Basketball/Pool Table/Fun
Reason: I changed the info since it's a house party now so I didn't want to rush to close. It is a guaranteed project though thx
21-40 year old house music lounge lovers
House

```html
<!DOCTYPE html>
<html lang="en">
<head>
<meta charset="utf-8">
<title>Tide Sway Pool Party Flyer</title>
<link rel="stylesheet" href="https://fonts.googleapis.com/css2?family=Luckiest+Guy&family=Pacifico&family=Oswald:wght@500;700&display=swap">
<style>
  :root {
    --sun-yellow: #ffd23a;
    --sun-orange: #f58a1f;
    --deep-orange: #e8661a;
    --sky-blue: #5fb4e6;
    --pool-blue: #1f8fd6;
    --navy: #123e86;
    --ink-blue: #1a64b8;
    --paper: #ffffff;
    --mist: #eaf5fc;
  }
  * { margin: 0; padding: 0; box-sizing: border-box; }
  html, body { width: 816px; height: 1200px; overflow: hidden; background: var(--paper); }
  .flyer {
    position: relative;
    width: 816px;
    height: 1200px;
    overflow: hidden;
    background: linear-gradient(180deg, var(--paper) 60%, var(--mist) 100%);
    font-family: "Oswald", "Arial Narrow", sans-serif;
  }
  .hero-photo {
    position: absolute;
    left: 0; top: 0;
    width: 816px; height: 660px;
    background: linear-gradient(180deg, var(--sun-orange) 0%, var(--sun-yellow) 38%, var(--sky-blue) 72%, var(--pool-blue) 88%, var(--paper) 100%);
  }
  .date-badge {
    position: absolute;
    right: 12px; top: 16px;
    padding: 8px 24px;
    background: var(--deep-orange);
    border-radius: 10px;
    color: var(--paper);
    font-weight: 700;
    font-size: 40px;
    letter-spacing: 1px;
    line-height: 1.1;
  }
  .headline {
    position: absolute;
    left: 0; right: 0; top: 540px;
    text-align: center;
  }
  .headline-main {
    display: block;
    font-family: "Luckiest Guy", "Impact", sans-serif;
    font-size: 112px;
    line-height: 1;
    color: var(--sun-yellow);
    -webkit-text-stroke: 5px var(--navy);
    paint-order: stroke fill;
    text-shadow: 0 6px 0 var(--navy);
    letter-spacing: 2px;
  }
  .headline-sub {
    display: block;
    margin-top: -6px;
    font-family: "Pacifico", "Brush Script MT", cursive;
    font-size: 78px;
    line-height: 1.15;
    color: var(--sun-orange);
    -webkit-text-stroke: 3px var(--paper);
    paint-order: stroke fill;
  }
  .headline-sub .accent { color: var(--ink-blue); }
  .featuring {
    position: absolute;
    left: 0; right: 0; top: 762px;
    text-align: center;
    color: var(--ink-blue);
    font-weight: 700;
    font-size: 26px;
    letter-spacing: 3px;
  }
  .dj-marks {
    position: absolute;
    left: 0; right: 0; top: 806px;
    display: flex;
    justify-content: center;
    gap: 110px;
    align-items: center;
  }
  .dj-mark {
    display: flex;
    align-items: center;
    gap: 14px;
    color: var(--navy);
    font-weight: 700;
    font-size: 60px;
    letter-spacing: 4px;
    line-height: 1;
  }
  .dj-mark .dot {
    width: 50px; height: 50px;
    border-radius: 50%;
    background: var(--navy);
  }
  .dj-names {
    position: absolute;
    left: 0; right: 0; top: 884px;
    text-align: center;
    font-weight: 700;
    font-size: 48px;
    letter-spacing: 1px;
    line-height: 1.1;
  }
  .dj-names .first { color: var(--pool-blue); }
  .dj-names .last { color: var(--navy); }
  .amenities {
    position: absolute;
    left: 0; right: 0; top: 952px;
    text-align: center;
    color: var(--ink-blue);
    font-weight: 500;
    font-size: 28px;
    letter-spacing: 1px;
  }
  .address-note {
    position: absolute;
    left: 0; right: 0; top: 1118px;
    text-align: center;
    color: var(--ink-blue);
    font-weight: 500;
    font-size: 20px;
    letter-spacing: 1px;
  }
</style>
</head>
<body>
<main class="flyer">
  <div class="hero-photo" role="img" aria-label="Photo of a woman in a white swimsuit at a pool edge with palm trees and a bright summer sky"></div>

  <div class="date-badge">JULY 13, 2013</div>

  <h1 class="headline">
    <span class="headline-main">TIDE SWAY</span>
    <span class="headline-sub">Pool <span class="accent">Party</span></span>
  </h1>

  <p class="featuring">FEATURING DJS</p>

  <div class="dj-marks">
    <div class="dj-mark">VANTOR</div>
    <div class="dj-mark"><span class="dot"></span>KEMBLE</div>
  </div>

  <p class="dj-names">
    <span class="first">LIONEL</span> <span class="last">HARTWICK</span>
    &nbsp;<span class="first">MARTY</span> <span class="last">OAKES</span>
  </p>

  <p class="amenities">FULL BAR/FOOD/WATER BASKETBALL/POOL TABLE/FUN</p>

  <p class="address-note">BRINDLEPAGE.COM/VANTOR87 FOR ADDRESS (LARKWOOD, INVITE ONLY)</p>
</main>
</body>
</html>
```